Billboard - Cool Garden and Landscape Company (Brand Pack Included)

NEED A PROFESSIONAL BILLBOARD TO ADVERTISE OUR BUSINESS. HAVE MOCKED UP A SAMPLE CONCEPT BUT IT REQUIRES THE ICONS TO BE DEVELOPED TO A PROFESSIONAL STANDARD (I JUST COPIED RANDOM EXAMPLES FROM THE NET)

THE ICONS REPRESENT OUR KEY PRODUCT GROUPS. (These can be redesigned)
BILLBOARD IS 6M X 3M (SEE SPEC FILE ATTACHED) - IMAGE OF THE LOCATION ADDED TO THE FILES.

BRAND GUIDE INCLUDED WITH LOGO FILES

VISIT: https://www.facebook.com/Crew.Moss.Crate/
Web: www.mosscrate.co.nz

Target Market(s)

Commuter traffic - busy road - Billboard site is on the left side approx 400m before our street turn off. Age group 30+ Home owners / Builders

Industry/Entity Type

Garden Supply

Font styles to use
Other font styles liked:
• comfortaa

Requirements
Must have
• No change to our logo or brand
• Next left
• Icons for products as per mock up - note these can be redesigned
Nice to have
• Easy to see at a distance
• Clean
• Simple

```html
<!DOCTYPE html>
<html lang="en">
<head>
<meta charset="utf-8">
<title>Moss Crate Billboard</title>
<link rel="stylesheet" href="https://fonts.googleapis.com/css2?family=Comfortaa:wght@400;700&family=Fira+Sans+Extra+Condensed:wght@700&family=Arimo:wght@700&display=swap">
<style>
  :root {
    --green: #0f9a46;
    --orange: #f49420;
    --white: #ffffff;
    --page: #e9ecee;
  }
  * { margin: 0; padding: 0; box-sizing: border-box; }
  html, body { width: 1200px; height: 905px; overflow: hidden; background: var(--page); }
  .billboard {
    position: absolute; left: 20px; top: 162px;
    width: 1160px; height: 580px;
    background: var(--white); overflow: hidden;
    box-shadow: 0 4px 18px rgba(0,0,0,.15);
  }
  .bands { position: absolute; inset: 0; }
  .brand {
    position: absolute; top: 26px; left: 0; right: 0;
    display: flex; flex-direction: column; align-items: center;
  }
  .brand-name {
    font-family: 'Arimo', sans-serif; font-weight: 700;
    font-size: 56px; letter-spacing: 1px; color: var(--green); line-height: 1;
  }
  .tagline-row { display: flex; align-items: center; gap: 12px; margin-top: 12px; }
  .tagline-rule { width: 160px; height: 3px; background: var(--orange); }
  .tagline {
    font-family: 'Comfortaa', sans-serif; font-weight: 400;
    font-size: 22px; letter-spacing: 1.5px; color: var(--orange);
  }
  .product { position: absolute; top: 150px; width: 210px; text-align: center; }
  .product svg { display: block; margin: 0 auto; }
  .product-label {
    margin-top: 6px;
    font-family: 'Fira Sans Extra Condensed', sans-serif; font-weight: 700;
    font-size: 30px; line-height: 1.05; color: var(--white);
  }
  .divider { position: absolute; top: 305px; width: 3px; height: 60px; background: var(--white); }
  .next-left { position: absolute; left: 60px; top: 380px; width: 530px; height: 80px; }
  .next-left-text {
    position: absolute; left: 68px; top: 10px;
    font-family: 'Comfortaa', sans-serif; font-weight: 700;
    font-size: 58px; color: var(--white); letter-spacing: 1px; line-height: 1;
  }
  .address {
    position: absolute; left: 600px; top: 392px; width: 520px;
    border-top: 2px solid var(--white); border-bottom: 2px solid var(--white);
    padding: 5px 0 7px;
    font-family: 'Comfortaa', sans-serif; font-weight: 400;
    font-size: 32px; color: var(--white); white-space: nowrap;
  }
  .supplies {
    position: absolute; left: 0; right: 0; top: 488px; text-align: center;
    font-family: 'Arimo', sans-serif; font-weight: 700;
    font-size: 34px; color: var(--green);
  }
</style>
</head>
<body>
<main class="billboard">
  <svg class="bands" width="1160" height="580" viewBox="0 0 1160 580" aria-hidden="true">
    <path d="M0,150 Q600,300 1160,140 L1160,470 L0,470 Z" fill="var(--orange)"/>
    <path d="M0,162 Q600,318 1160,158" fill="none" stroke="var(--green)" stroke-width="7"/>
    <path d="M0,445 L1160,450" stroke="var(--white)" stroke-width="3"/>
    <path d="M0,572 Q600,560 1160,518 L1160,580 L0,580 Z" fill="var(--orange)"/>
    <path d="M0,566 Q600,554 1160,512" fill="none" stroke="var(--orange)" stroke-width="2"/>
  </svg>

  <header class="brand">
    <span class="brand-name">MOSS CRATE</span>
    <div class="tagline-row">
      <span class="tagline-rule"></span>
      <span class="tagline">Grow Something Good</span>
    </div>
  </header>

  <section class="product" style="left:112px">
    <svg width="140" height="150" viewBox="0 0 140 150" role="img" aria-label="Firewood and fire pellets icon">
      <polygon points="70,3 135,40 135,110 70,147 5,110 5,40" fill="var(--green)" stroke="var(--white)" stroke-width="4"/>
    </svg>
    <p class="product-label">FIREWOOD<br>FIRE PELLETS</p>
  </section>
  <span class="divider" style="left:330px"></span>

  <section class="product" style="left:337px">
    <svg width="140" height="150" viewBox="0 0 140 150" role="img" aria-label="Compost, soil and mulch icon">
      <polygon points="70,3 135,40 135,110 70,147 5,110 5,40" fill="var(--green)" stroke="var(--white)" stroke-width="4"/>
    </svg>
    <p class="product-label">COMPOST<br>SOIL + MULCH</p>
  </section>
  <span class="divider" style="left:558px"></span>

  <section class="product" style="left:560px; width:240px">
    <svg width="140" height="150" viewBox="0 0 140 150" role="img" aria-label="Decorative stone aggregates icon">
      <polygon points="70,3 135,40 135,110 70,147 5,110 5,40" fill="var(--green)" stroke="var(--white)" stroke-width="4"/>
    </svg>
    <p class="product-label">DECORATIVE<br>STONE AGGREGATES</p>
  </section>
  <span class="divider" style="left:812px"></span>

  <section class="product" style="left:822px; width:250px">
    <svg width="140" height="150" viewBox="0 0 140 150" role="img" aria-label="Trailer hire and delivery icon">
      <polygon points="70,3 135,40 135,110 70,147 5,110 5,40" fill="var(--green)" stroke="var(--white)" stroke-width="4"/>
    </svg>
    <p class="product-label">HIRE<br>TRAILERS DELIVERY</p>
  </section>

  <div class="next-left">
    <svg width="530" height="80" viewBox="0 0 530 80" aria-hidden="true">
      <path d="M0,40 L48,0 L40,12 L525,12 L500,42 L525,72 L40,72 L48,80 Z" fill="var(--green)"/>
      <path d="M495,16 L472,42 L495,68 M510,16 L487,42 L510,68" fill="none" stroke="var(--white)" stroke-width="4"/>
    </svg>
    <span class="next-left-text">NEXT LEFT</span>
  </div>

  <p class="address">42 Harlow Road (off Penfold)</p>

  <p class="supplies">Garden &amp; Landscape Supplies</p>
</main>
</body>
</html>
```